MODELS AGENCY NEW YEAR 2026 CARD

A 10 cm x 21 cm horizontal New Year card for clients of our 2 models agencies, Pommelin (kids) and Velvaride (actors and adults) (logo in the jobs).

Side A of the card: creative mission:
-text: 2026
-text: Peace and Love
-Studio or movie set atmosphere
-tone of voice: optimistic, positive, colorful

Side B:
(name of 4 people of the agency:)
Odette, Anne-Sophie, Hortense & Luc-Antoine,
(2 logos)
Pommelin & VelvaRide
(Adres)
Rue des Tilleuls 74 b3 - 1200 Bruxelles - Belgique

Target Market(s)

Movie directors, photographers

Industry/Entity Type

Fashion, advertising & Movies

Requirements
Must have
• SEE TEXT IN BRIEFING

```html
<!DOCTYPE html>
<html lang="fr">
<head>
<meta charset="utf-8">
<title>Pommelin &amp; VelvaRide – New Year 2026</title>
<link rel="stylesheet" href="https://fonts.googleapis.com/css2?family=Arimo:wght@400;700&display=swap">
<style>
  :root {
    --page-bg: #cacbca;
    --card-white: #ffffff;
    --blue: #1a9ee0;
    --orange: #ef8240;
    --purple: #3c2069;
    --kid-orange: #ef5a1a;
    --ink: #2a2a2a;
    --muted: #555555;
    --line: #7cc6ee;
    --night-top: #2a1646;
    --night-bottom: #100a1c;
    --headline: #ffffff;
  }
  * { margin: 0; padding: 0; box-sizing: border-box; }
  html, body { width: 1200px; height: 1200px; overflow: hidden; background: var(--page-bg); }
  .canvas { position: relative; width: 1200px; height: 1200px; }
  .card {
    position: absolute; left: 14px; top: 321px; width: 1172px; height: 558px;
    display: flex; box-shadow: 0 1px 3px rgba(0,0,0,.12);
    font-family: "Arimo", Arial, sans-serif;
  }
  .side-contacts { position: relative; width: 586px; height: 100%; background: var(--card-white); }
  .side-greeting { position: relative; flex: 1; height: 100%; overflow: hidden; }

  .team { position: absolute; top: 66px; left: 0; right: 0; text-align: center; font-size: 29px; line-height: 38px; }
  .team .row-a { color: var(--blue); }
  .team .row-b { color: var(--orange); }

  .agency { position: absolute; top: 258px; width: 230px; text-align: center; }
  .agency.kids { left: 70px; }
  .agency.adults { left: 308px; }
  .agency-mark { display: flex; align-items: center; justify-content: center; gap: 8px; font-weight: 700; font-size: 32px; line-height: 40px; color: var(--purple); }
  .agency-mark .dot { width: 12px; height: 12px; border-radius: 50%; }
  .kids .dot { background: var(--blue); }
  .adults .dot { background: var(--kid-orange); }
  .agency-tag { margin-top: 8px; font-size: 10px; letter-spacing: 1.1px; color: var(--purple); text-transform: uppercase; }
  .agency-since { margin-top: 44px; font-size: 7.5px; letter-spacing: .6px; color: var(--muted); text-transform: uppercase; }

  .locator { position: absolute; top: 414px; left: 76px; width: 450px; height: 40px; }
  .address { position: absolute; top: 460px; left: 0; right: 0; text-align: center; color: var(--ink); font-size: 23.5px; line-height: 34px; }

  .night-photo { position: absolute; inset: 0;
    background:
      radial-gradient(ellipse 60% 25% at 55% 88%, rgba(240,170,70,.35), transparent 70%),
      radial-gradient(ellipse 40% 22% at 60% 70%, rgba(220,120,200,.28), transparent 70%),
      linear-gradient(180deg, var(--night-top) 0%, #24123e 55%, var(--night-bottom) 100%);
  }
  .headline { position: absolute; top: 92px; left: 0; right: 0; text-align: center; color: var(--headline); }
  .headline-kicker { font-size: 34px; line-height: 40px; letter-spacing: 1px; }
  .headline-year { margin-top: 6px; font-weight: 700; font-size: 120px; line-height: 124px; letter-spacing: 4px; }
  .headline-motto { margin-top: 8px; font-size: 32px; line-height: 38px; letter-spacing: 6px; text-transform: uppercase; }
</style>
</head>
<body>
<div class="canvas">
  <div class="card">
    <section class="side-contacts">
      <div class="team">
        <div class="row-a">Odette, Anne-Sophie</div>
        <div class="row-b">Hortense &amp; Luc-Antoine</div>
      </div>

      <div class="agency kids">
        <div class="agency-mark"><span class="dot"></span>Pommelin</div>
        <div class="agency-tag">Children models agency</div>
        <div class="agency-since">– Since 1982 –</div>
      </div>

      <div class="agency adults">
        <div class="agency-mark"><span class="dot"></span>VelvaRide</div>
        <div class="agency-tag">People, actors &amp; models agency</div>
        <div class="agency-since">– Since 2000 –</div>
      </div>

      <svg class="locator" viewBox="0 0 450 40" aria-hidden="true">
        <line x1="0" y1="19" x2="195" y2="19" stroke="var(--line)" stroke-width="1.2"/>
        <line x1="255" y1="19" x2="450" y2="19" stroke="var(--line)" stroke-width="1.2"/>
        <path d="M225 38 C216 27 209 20 209 12 A16 16 0 0 1 241 12 C241 20 234 27 225 38 Z" fill="var(--blue)"/>
        <circle cx="225" cy="12" r="6" fill="#fff"/>
      </svg>

      <div class="address">
        <div>Rue des Tilleuls 74 b3 - 1200</div>
        <div>Bruxelles - Belgique</div>
      </div>
    </section>

    <section class="side-greeting">
      <div class="night-photo" role="img" aria-label="Night photograph of a city skyline with colourful fireworks bursting above the lights"></div>
      <div class="headline">
        <div class="headline-kicker">Creative Mission</div>
        <div class="headline-year">2026</div>
        <div class="headline-motto">Peace and Love</div>
      </div>
    </section>
  </div>
</div>
</body>
</html>
```